IT-Dienstleister für Projektmanagementsoftware sucht Broschüre im DIN-A4-Format
Zielgruppe
Wir sind ein IT-Dienstleister für Projektmanagementsoftware. Wir installieren, migrieren und entwickeln Software für das Projektmanagement auf Basis von Veltrano Technologien. Unsere Zielgruppe sind mittelständische Unternehmen und große Konzerne. Je komplexer das Projektmanagement in einem Unternehmen, desto eher helfen unsere Lösungen.
Aufgabenstellung
Es soll eine DIN A4 Hochglanz Broschüre für eine Messe entstehen. Wir haben bereits ein Grobkonzept mit Bildauswahl und Texten erstellt. An diesem soll sich orientiert werden. Bezüglich desDesigns, der Anordnung der Texte und Bilder etc. besteht völlige Freiheit. Weitere Orientierung bieten unsere Webseiten haldewiegand.de und quilbyte.de. Die Texte und Screenshots sind teilweise nur Platzhalter und müssen später noch angepasst werden können. Wir benötigen daher unbedingt die Rohdaten des Designs.

```html
<!DOCTYPE html>
<html lang="de">
<head>
<meta charset="utf-8">
<title>Broschüre – Gentle Bison &amp; Cautious Viper</title>
<link href="https://fonts.googleapis.com/css2?family=Roboto:wght@300;400;500;700&family=Arimo:wght@400;700&display=swap" rel="stylesheet">
<style>
:root{
  --stage:#e4e4e4;
  --paper:#ffffff;
  --green:#9cc43c;
  --ink:#1e1e1e;
  --white:#ffffff;
  --shot:#eef0f2;
  --shot-line:#d3d7db;
}
*{margin:0;padding:0;box-sizing:border-box}
html,body{width:1200px;height:848px;overflow:hidden;background:var(--stage)}
.spread{position:absolute;left:40px;top:28px;width:1120px;height:792px;display:flex;box-shadow:0 10px 30px rgba(0,0,0,.18)}
.page{position:relative;width:560px;height:792px;background:var(--paper);overflow:hidden}
.page--left{box-shadow:inset -14px 0 18px -14px rgba(0,0,0,.18)}
.page--right{box-shadow:inset 14px 0 18px -14px rgba(0,0,0,.18)}
.band{position:absolute;left:0;top:0;width:560px;height:360px}
.title{position:absolute;left:56px;font-family:"Roboto",sans-serif;font-weight:300;font-size:37px;line-height:44px;color:var(--white);letter-spacing:.2px;white-space:nowrap}
.subtitle{position:absolute;left:56px;font-family:"Arimo",sans-serif;font-size:14px;line-height:19px;color:var(--white);white-space:nowrap}
.intro{position:absolute;left:56px;font-family:"Arimo",sans-serif;font-size:9.6px;line-height:14px;color:var(--ink);white-space:nowrap}
.overview{position:absolute;left:56px;font-family:"Arimo",sans-serif;color:var(--ink)}
.overview h3{font-size:10px;font-weight:700;margin-bottom:16px}
.overview ul{list-style:none}
.overview li{position:relative;padding-left:14px;font-size:10px;line-height:13.5px;margin-bottom:6px;white-space:nowrap}
.overview li::before{content:"»";position:absolute;left:0;top:0}
.screenshot{position:absolute;border:1px solid var(--shot-line)}
</style>
</head>
<body>
<main class="spread">

  <section class="page page--left">
    <svg class="band" viewBox="0 0 560 360" role="img" aria-label="Grünes Titelband mit Foto eines zotteligen Hochlandrinds mit langen Hörnern auf einer Wiese vor bewölktem Himmel">
      <defs>
        <linearGradient id="bandLeft" x1="0" y1="0" x2="0" y2="1">
          <stop offset="0" stop-color="#96c034"/>
          <stop offset="1" stop-color="#a8cd48"/>
        </linearGradient>
        <linearGradient id="bisonTone" x1="0" y1="0" x2="1" y2="0">
          <stop offset="0" stop-color="#9cc43c" stop-opacity="0"/>
          <stop offset=".45" stop-color="#8a8a5a" stop-opacity=".75"/>
          <stop offset="1" stop-color="#7d8a76" stop-opacity=".9"/>
        </linearGradient>
        <linearGradient id="bisonFade" x1="0" y1="0" x2="0" y2="1">
          <stop offset=".55" stop-color="#a4c944" stop-opacity="0"/>
          <stop offset="1" stop-color="#a8cd48" stop-opacity="1"/>
        </linearGradient>
        <clipPath id="bandLeftClip"><polygon points="0,0 560,0 560,310 0,340"/></clipPath>
      </defs>
      <g clip-path="url(#bandLeftClip)">
        <rect width="560" height="360" fill="url(#bandLeft)"/>
        <rect x="250" width="310" height="330" fill="url(#bisonTone)"/>
        <rect x="250" width="310" height="330" fill="url(#bisonFade)"/>
      </g>
    </svg>

    <h1 class="title" style="top:92px">Gentle Bison</h1>
    <p class="subtitle" style="top:145px">Digitalisierung Ihres&nbsp; Ressourcen-<br>genehmigungsprozess in Veltrano Project</p>
    <p class="intro" style="top:204px">Gentle Bison unterstützt die Kommunikation zwischen<br>Ressourcenmanagern und Projektleitern. Der Bedarf und<br>die Freigabe von Ressourcen wird durch Gentle Bison zentral<br>und unabhängig verwaltet und mögliche Abweichungen<br>transparent abgebildet.</p>

    <div class="overview" style="top:372px">
      <h3>Alles auf einen Blick:</h3>
      <ul>
        <li>Digitalisierung des Ressour-<br>cenfreigabeprozesses</li>
        <li>Erhöhte Transparenz der<br>Planung und Freigabe</li>
        <li>Live Daten</li>
        <li>Unabhängigkeit der<br>Planung und Freigabe</li>
        <li>Vereinfachte<br>Kommunikation</li>
        <li>Reine Planweb App<br>Nutzung möglich</li>
        <li>Integration in Planwerk<br>Professional</li>
      </ul>
    </div>

    <svg class="screenshot" style="left:212px;top:368px;width:292px;height:170px" viewBox="0 0 292 170" role="img" aria-label="Bildschirmfoto der Ressourcenplanung mit Freigabedialog">
      <rect width="292" height="170" fill="var(--shot)"/>
    </svg>
    <svg class="screenshot" style="left:190px;top:556px;width:314px;height:145px" viewBox="0 0 314 145" role="img" aria-label="Bildschirmfoto der Ressourcenanfrage mit Genehmigungsfenster">
      <rect width="314" height="145" fill="var(--shot)"/>
    </svg>
  </section>

  <section class="page page--right">
    <svg class="band" viewBox="0 0 560 360" role="img" aria-label="Grünes Titelband mit Foto einer gemusterten Schlange, eingerollt zwischen trockenem Laub">
      <defs>
        <linearGradient id="bandRight" x1="0" y1="0" x2="0" y2="1">
          <stop offset="0" stop-color="#96c034"/>
          <stop offset="1" stop-color="#aed052"/>
        </linearGradient>
        <linearGradient id="viperTone" x1="0" y1="0" x2="1" y2="0">
          <stop offset="0" stop-color="#9cc43c" stop-opacity="0"/>
          <stop offset=".4" stop-color="#c8c89a" stop-opacity=".7"/>
          <stop offset="1" stop-color="#bdb79a" stop-opacity=".9"/>
        </linearGradient>
        <linearGradient id="viperFade" x1="0" y1="0" x2="0" y2="1">
          <stop offset=".5" stop-color="#a8cc4a" stop-opacity="0"/>
          <stop offset="1" stop-color="#aed052" stop-opacity="1"/>
        </linearGradient>
        <clipPath id="bandRightClip"><polygon points="0,0 560,0 560,280 0,310"/></clipPath>
      </defs>
      <g clip-path="url(#bandRightClip)">
        <rect width="560" height="360" fill="url(#bandRight)"/>
        <rect x="250" width="310" height="290" fill="url(#viperTone)"/>
        <rect x="250" width="310" height="290" fill="url(#viperFade)"/>
      </g>
    </svg>

    <h1 class="title" style="top:86px">Cautious Viper</h1>
    <p class="subtitle" style="top:140px">Risiko- und Issueportfolio<br>übersichtlich dargestellt</p>
    <p class="intro" style="top:199px">Cautious Viper dient zur grafischen und tabellarischen<br>Aufbereitung des Risiko- und Issueportfolios. Damit werden<br>kritische Zustände in Ihren Projekten noch schneller erkannt.<br>Risiken und Issues können so spezifisch adressiert werden.</p>

    <div class="overview" style="top:369px">
      <h3>Alles auf einen Blick:</h3>
      <ul>
        <li>Überblick über das gesamte<br>Risiko- und Issueportfolio</li>
        <li>Click-to-Filter-Möglichkeit<br>in der Matrix</li>
        <li>Export nach Veltrano Tabula</li>
        <li>Risk-to-Issue-Eskalation</li>
        <li>Beziehung zwischen Risks<br>und Issues</li>
      </ul>
    </div>

    <svg class="screenshot" style="left:230px;top:358px;width:298px;height:158px" viewBox="0 0 298 158" role="img" aria-label="Bildschirmfoto der Risikomatrix mit Risikotabelle">
      <rect width="298" height="158" fill="var(--shot)"/>
    </svg>
    <svg class="screenshot" style="left:230px;top:538px;width:298px;height:162px" viewBox="0 0 298 162" role="img" aria-label="Bildschirmfoto der gefilterten Risikomatrix">
      <rect width="298" height="162" fill="var(--shot)"/>
    </svg>
  </section>

</main>
</body>
</html>
```